KVR Power Works ( LED lIghting Service Company) flyer

A single sheet folded in half, like a book, highlighting LED lighting retrofits. Use stock pictures for different bulbs. We sell and install all fixtures. We install 48" tubes, corn bulbs, UFO lights, high bay lights, gas station canopy lights, parking lot lights,
Should include:
Reduce electric bill by as much as 70%
Improved quality of light
Zero maintenance cost
Eliminates eye strain and headache pain
Produces no heat
5 year warranty
Work with power companies to achieve greatest rebate.
Complete turnkey solution provider
Target Market(s)
Business owners, facility managers, VP of operations
Industry/Entity Type
It Company
Colors
Designer to choose colors to be used in the design.
Requirements
Must have
- High quality photos,
Nice to have
- Fonts, colors and designs are up to the designers

```html
<!DOCTYPE html>
<html lang="en">
<head>
<meta charset="utf-8">
<title>KVR Power Works – LED Lighting Retrofit Folder</title>
<link href="https://fonts.googleapis.com/css2?family=Russo+One&family=Roboto:wght@400;700&display=swap" rel="stylesheet">
<style>
  :root{
    --page-bg:#e4e4e6;
    --ink-black:#050505;
    --paper:#f2f2f2;
    --brand-blue:#1690c4;
    --text-dark:#1b1b1b;
    --text-light:#e8e8e8;
    --photo-glow:#e0602a;
    --photo-dark:#2f3844;
  }
  *{margin:0;padding:0;box-sizing:border-box}
  html,body{width:1200px;height:840px;overflow:hidden;background:var(--page-bg)}
  .folder{position:absolute;left:60px;top:40px;width:1080px;height:760px;display:flex;box-shadow:0 10px 30px rgba(0,0,0,.18)}
  .panel{position:relative;width:540px;height:760px;overflow:hidden}

  /* back panel */
  .panel--back{background:var(--ink-black);color:var(--text-light)}
  .brand{position:absolute;font-family:"Roboto",sans-serif;font-weight:700;color:var(--brand-blue);line-height:1}
  .panel--back .brand{left:40px;top:70px;font-size:36px}
  .brand-sub{display:block;font-size:13px;letter-spacing:2px;margin-top:6px}
  .divider{position:absolute;left:250px;top:55px;width:1px;height:110px;background:#777}
  .contact-list{position:absolute;left:280px;top:62px;list-style:none;font-family:"Roboto",sans-serif;font-size:13px}
  .contact-list li{display:flex;align-items:center;gap:14px;height:25px}
  .contact-list svg{width:12px;height:12px;fill:var(--brand-blue);flex:none}
  .back-photo{position:absolute;left:0;top:200px;width:540px;height:560px;
    background:radial-gradient(ellipse 55% 45% at 50% 45%,#fff3d8 0%,var(--photo-glow) 28%,#7a2a10 55%,var(--ink-black) 80%)}

  /* front panel */
  .panel--front{background:var(--paper)}
  .front-art{position:absolute;inset:0}
  .panel--front .brand{left:40px;top:345px;font-size:50px}
  .panel--front .brand-sub{font-size:12px;color:var(--text-dark);letter-spacing:1.5px}
  .headline{position:absolute;left:40px;top:450px;font-family:"Russo One",sans-serif;color:var(--brand-blue);font-size:62px;letter-spacing:3px;line-height:1}
  .subhead{position:absolute;left:42px;top:520px;font-family:"Roboto",sans-serif;color:var(--text-dark);font-size:37px;letter-spacing:1px;line-height:1}
  .web-band{position:absolute;left:60px;top:600px;width:300px;height:26px;background:var(--brand-blue);color:#fff;
    font-family:"Roboto",sans-serif;font-size:12px;letter-spacing:3px;display:flex;align-items:center;justify-content:center}
</style>
</head>
<body>
<main class="folder">
  <section class="panel panel--back">
    <div class="brand">KVR<span class="brand-sub">POWER WORKS</span></div>
    <div class="divider"></div>
    <ul class="contact-list">
      <li><svg viewBox="0 0 12 12"><path d="M6 0a4 4 0 0 0-4 4c0 3 4 8 4 8s4-5 4-8a4 4 0 0 0-4-4zm0 5.5A1.5 1.5 0 1 1 6 2.5a1.5 1.5 0 0 1 0 3z"/></svg>your address</li>
      <li><svg viewBox="0 0 12 12"><path d="M2.5 0l2 2.5-1.2 1.5c.8 1.8 2.2 3.2 4 4L8.8 6.8 11.3 8.8 10 11c-5 0-9-4-9-9z"/></svg>123 456 7890</li>
      <li><svg viewBox="0 0 12 12"><path d="M0 2h12v8H0zm1 1v.4l5 3.3 5-3.3V3z"/></svg>info@kvrpowerworks.com</li>
      <li><svg viewBox="0 0 12 12"><circle cx="6" cy="6" r="6"/></svg>www.kvrpowerworks.com</li>
    </ul>
    <div class="back-photo" role="img" aria-label="Photo of cupped hands holding a glowing spiral energy-saving bulb"></div>
  </section>

  <section class="panel panel--front">
    <svg class="front-art" viewBox="0 0 540 760" aria-hidden="false">
      <defs>
        <linearGradient id="heroTone" x1="0" y1="0" x2="1" y2="1">
          <stop offset="0" stop-color="#5a6572"/>
          <stop offset="1" stop-color="var(--photo-dark)"/>
        </linearGradient>
      </defs>
      <polygon points="540,60 540,410 310,410 310,425 540,425 540,440 290,440 290,410" fill="var(--brand-blue)"/>
      <polygon role="img" aria-label="Photo of a hand in a suit sleeve holding up a lit spiral bulb against dark wood" points="100,230 170,55 520,55 540,150 540,400 220,400" fill="url(#heroTone)"/>
      <polygon points="540,690 540,760 400,760" fill="var(--brand-blue)"/>
      <line x1="395" y1="757" x2="540" y2="684" stroke="var(--ink-black)" stroke-width="4"/>
    </svg>
    <div class="brand">KVR<span class="brand-sub">POWER WORKS</span></div>
    <h1 class="headline">TRUSTED LED</h1>
    <p class="subhead">LIGHTING RETROFITTERS</p>
    <div class="web-band">www.kvrpowerworks.net</div>
  </section>
</main>
</body>
</html>
```